Brookvale Insurance Services - Insurance Agency Wesbite

I need a website for my insurance agency called Brookvale Insurance Services. I have attached my company logo. You can use the colors from the copy logo to create the website color scheme. I need a Request A Quote section.
Business Address: 7316 Marlowe Ave Unit D, Studio City Ca 91607
Business Phone: (818) 555-0193
I would need the following drop downs on the main page:

1st drop down:
Business Insurance
⁃ Commercial Auto
⁃ Employment Practice Liability Insurance
⁃ General Liability Insurance
⁃ Professional Liability Insurance
⁃ Property Insurance
⁃ Workers Compensation Insurance

2nd drop down:
Industries We Serve
- Construction
- Janitorial
- Landscapers
- Trucking
- ParcelWay Independent Service Providers (ISP)
Healthcare Industry
- Community Care Facilities
- Home Health Agencies
- Hospice
- Nursing Homes

3rd drop down:
Risk Management
- Claims Management
- Compliance & Risk Management

4th drop down
Request a quote

5th drop down
About Us

6th drop down
Contact US

Target Market(s)

Potential clients

Industry/Entity Type

Business Insurance

Coding

Coded - Design and coding required

Number of Pages Required

5+ page

Colors
0054AA
0677BA
7BADD7
CADEEF
E8F1F8
00AB8E
00BBA5
67D7C9
C6EFE9
E9F9F6

Requirements
Must have
• Home Business Insurance - Commercial Auto - Employment Practice Liability Insurance - General Liability Insurance - Professional Liability Insurance - Property Insurance - Workers Compensation Insurance Industries We Serve - Construction - Janitorial - Landscapers - Manufacturing Companies - Restaurants - Towing - Trucking Healthcare Industry - Community Care Facilities - Home Health Agencies - Hospice - Nursing Homes - Risk Management - Claims Management - Compliance & Risk Management Request a Quote About Us Contact Us

```html
<!DOCTYPE html>
<html lang="en">
<head>
<meta charset="utf-8">
<title>Brookvale Insurance Services</title>
<link href="https://fonts.googleapis.com/css2?family=Montserrat:wght@400;500;600;700&display=swap" rel="stylesheet">
<style>
:root{
  --navy:#0b2b8c;
  --navy-deep:#0a2577;
  --green:#15982d;
  --hero:#2c3b57;
  --text:#333a44;
  --muted:#6b6f76;
  --white:#ffffff;
  --quote:#5f9a6a;
}
*{margin:0;padding:0;box-sizing:border-box}
html,body{width:1200px;height:3281px;overflow:hidden}
body{font-family:'Montserrat',sans-serif;color:var(--text);background:var(--white);position:relative}
.abs{position:absolute}
/* header */
.site-header{left:0;top:0;width:1200px;height:86px;background:var(--white)}
.brand{left:111px;top:20px;color:var(--navy);font-weight:700;line-height:1}
.brand .name{font-size:25px;letter-spacing:.5px;display:block}
.brand .sub{font-size:10px;letter-spacing:3px;display:block;margin-top:6px}
.main-nav{right:111px;top:34px;display:flex;gap:18px;font-size:14px;font-weight:500;color:#1b1f27}
/* hero */
.hero{left:0;top:86px;width:1200px;height:612px}
.hero-text{left:111px;top:194px;color:var(--white);width:440px}
.hero-text .eyebrow{font-size:27px;font-weight:500}
.hero-text h1{font-size:45px;font-weight:700;line-height:1.05;margin-top:18px}
.hero-text p{font-size:16px;line-height:26px;margin-top:20px;width:395px}
/* section heading */
.section-title{width:1200px;left:0;text-align:center;font-size:40px;font-weight:600;color:var(--green)}
/* cards */
.card{top:860px;width:298px;height:302px}
.card .photo{width:298px;height:250px}
.card .label{height:52px;background:var(--navy);color:var(--white);font-size:22px;font-weight:600;display:flex;align-items:center;justify-content:center}
.btn{display:flex;align-items:center;justify-content:center;color:var(--white);font-size:15px;font-weight:500}
.view-more{left:534px;top:1204px;width:132px;height:42px;background:var(--green)}
/* about */
.about-bg{left:0;top:1333px;width:1200px;height:518px}
.about-card{left:111px;top:1419px;width:421px;height:284px;background:var(--white);border-radius:22px;padding:36px 19px 0 20px}
.about-card h2{text-align:center;font-size:40px;font-weight:600;color:var(--green)}
.about-card p{font-size:15px;line-height:26px;margin-top:24px;color:var(--text)}
.link{font-size:14px;font-weight:500;text-decoration:underline;color:var(--green);display:inline-block}
.about-card .link{margin-top:8px}
/* risk */
.risk-item{top:2017px;width:470px}
.risk-head{display:flex;align-items:center;gap:18px}
.risk-icon{width:90px;height:81px;background:var(--navy);display:flex;align-items:center;justify-content:center}
.risk-head h3{font-size:22px;font-weight:600;color:#6f7378}
.risk-item p{font-size:15.5px;line-height:26px;margin-top:20px;color:var(--text)}
.risk-item .link{margin-top:12px}
/* quote */
.quote-bg{left:0;top:2329px;width:1200px;height:622px}
.quote-title{color:var(--white)}
.field{background:var(--white);font-size:15px;color:#444;padding:0 15px;display:flex;align-items:center}
.field.msg{align-items:flex-start;padding-top:14px}
.submit{left:508px;top:2765px;width:184px;height:41px;background:var(--navy)}
/* footer */
.footer{left:0;top:2879px;width:1200px;height:402px}
.foot-brand{left:111px;top:3019px;color:var(--white);font-weight:700;line-height:1}
.foot-brand .name{font-size:28px;display:block;letter-spacing:.5px}
.foot-brand .sub{font-size:11px;letter-spacing:3.5px;display:block;margin-top:8px}
.contact{color:var(--white);font-size:15px;line-height:25px}
.foot-h{color:var(--white);font-size:20px;font-weight:600}
.foot-p{color:var(--white);font-size:14.5px;line-height:26px}
.email{left:490px;top:3129px;width:234px;height:42px;background:#d6e2ff;color:#444;font-size:16px;padding-left:16px;display:flex;align-items:center}
.send{left:724px;top:3129px;width:62px;height:42px;background:var(--green)}
.social{left:889px;top:3065px;display:flex;gap:17px}
.social span{width:34px;height:34px;border:2px solid var(--white);border-radius:50%}
.foot-links{left:888px;top:3112px;color:var(--white);font-size:15px;line-height:26px}
.rule{left:111px;top:3232px;width:978px;height:1px;background:#8a9bd0}
.copy{left:0;top:3244px;width:1200px;text-align:center;color:var(--white);font-size:15.5px}
</style>
</head>
<body>

<header class="site-header abs">
  <div class="brand abs"><span class="name">BROOKVALE</span><span class="sub">INSURANCE SERVICES</span></div>
  <nav class="main-nav abs">
    <span>Business Insurance</span><span>Industries We Serve</span><span>Healthcare Industry</span><span>Risk Management</span><span>About Us</span><span>Contact Us</span>
  </nav>
</header>

<section class="hero abs">
  <svg width="1200" height="612" role="img" aria-label="Businessman's hands sheltering a glowing house icon">
    <defs>
      <linearGradient id="heroGrad" x1="0" x2="1" y1="0" y2="0">
        <stop offset="0" stop-color="#2e3d5a"/><stop offset=".6" stop-color="#2a3a58"/><stop offset="1" stop-color="#465673"/>
      </linearGradient>
    </defs>
    <polygon points="0,0 1200,0 1200,523 600,612 0,523" fill="var(--green)"/>
    <polygon points="0,0 1200,0 1200,512 600,588 0,512" fill="url(#heroGrad)"/>
  </svg>
  <div class="hero-text abs">
    <div class="eyebrow">Welcome To</div>
    <h1>Brookvale<br>Insurance Services</h1>
    <p>Lorem ipsum dolor sit amet, consectetur adipisc elit, sed do eiusmod tempor incididunt ut labore et dolore magna aliqua.</p>
  </div>
</section>

<h2 class="section-title abs" style="top:772px">Business Insurance</h2>

<div class="card abs" style="left:111px">
  <div class="photo" role="img" aria-label="Row of parked cars" style="background:linear-gradient(135deg,#c9ccd2,#8a2a2e 45%,#2a3140)"></div>
  <div class="label">Commercial Auto</div>
</div>
<div class="card abs" style="left:450px">
  <div class="photo" role="img" aria-label="Hands covering a model house" style="background:linear-gradient(180deg,#efe7e2,#d9b7a6 55%,#b8bcc4)"></div>
  <div class="label">Property Insurance</div>
</div>
<div class="card abs" style="left:789px">
  <div class="photo" role="img" aria-label="Businessman working on a laptop" style="background:linear-gradient(135deg,#dbd9d6,#8d8276 55%,#5b5f66)"></div>
  <div class="label">General Liability</div>
</div>
<div class="btn view-more abs">VIEW MORE</div>

<section class="about-bg abs">
  <svg width="1200" height="518" role="img" aria-label="Hands holding a glowing shield with family, home, car, health and savings icons">
    <defs>
      <radialGradient id="aboutGrad" cx=".63" cy=".45" r=".55">
        <stop offset="0" stop-color="#3e6fc4"/><stop offset=".6" stop-color="#153785"/><stop offset="1" stop-color="#0b2470"/>
      </radialGradient>
    </defs>
    <polygon points="0,0 1200,0 1200,447 600,518 0,447" fill="url(#aboutGrad)"/>
  </svg>
  <div class="about-card abs" style="left:111px;top:86px">
    <h2>About Us</h2>
    <p>Lorem ipsum dolor sit amet, consectetur adipiscing elit, sed do eiusmod tempor incididunt ut labore et dolore magna aliqua. Quis ipsum suspendisse ultrices gravida. Risus commodo</p>
    <span class="link">READ MORE</span>
  </div>
</section>

<h2 class="section-title abs" style="top:1927px">Risk Management</h2>

<div class="risk-item abs" style="left:112px">
  <div class="risk-head">
    <div class="risk-icon"><svg width="50" height="54" viewBox="0 0 50 54" fill="none" stroke="#fff" stroke-width="2"><rect x="6" y="5" width="30" height="42"/><path d="M12 15h18M12 22h18M12 29h12M12 36h8"/><path d="M44 14 28 40l-3 7 6-5 16-26z"/></svg></div>
    <h3>Claims Management</h3>
  </div>
  <p>Lorem ipsum dolor sit amet, consectetur adipisc elit, sed do eiusmod tempor incididunt ut labore et dolore magna aliqua. Quis ipsum suspendisse ultrices gravida. Risus commodo nas accumsan lacus vel facilisis.</p>
  <span class="link">LEARN MORE</span>
</div>
<div class="risk-item abs" style="left:618px">
  <div class="risk-head">
    <div class="risk-icon"><svg width="50" height="54" viewBox="0 0 50 54" fill="none" stroke="#fff" stroke-width="2"><rect x="10" y="4" width="26" height="36"/><rect x="5" y="9" width="26" height="38"/><path d="M11 18h14M11 24h14M11 30h8"/><circle cx="34" cy="40" r="9"/><path d="M30 40l3 3 5-6"/></svg></div>
    <h3>Compliance &amp; Risk Management</h3>
  </div>
  <p>Lorem ipsum dolor sit amet, consectetur adipisc elit, sed do eiusmod tempor incididunt ut labore et dolore magna aliqua. Quis ipsum suspendisse ultrices gravida. Risus commodo nas accumsan lacus vel facilisis.</p>
  <span class="link">LEARN MORE</span>
</div>

<section class="quote-bg abs">
  <svg width="1200" height="622" role="img" aria-label="Parent and child playing outdoors on a lawn, tinted green">
    <defs>
      <linearGradient id="quoteGrad" x1="0" x2="1" y1="0" y2="1">
        <stop offset="0" stop-color="#6fa277"/><stop offset=".55" stop-color="#4f8a55"/><stop offset="1" stop-color="#3f7a48"/>
      </linearGradient>
    </defs>
    <rect width="1200" height="622" fill="url(#quoteGrad)"/>
  </svg>
</section>

<section class="footer abs">
  <svg width="1200" height="474" style="position:absolute;top:-72px;left:0" aria-hidden="true">
    <polygon points="0,0 600,72 1200,0 1200,474 0,474" fill="var(--navy)"/>
  </svg>
</section>

<h2 class="section-title quote-title abs" style="top:2400px">Request A Quote</h2>
<div class="field abs" style="left:149px;top:2483px;width:435px;height:41px">First Name*</div>
<div class="field abs" style="left:617px;top:2483px;width:434px;height:41px">Last Name*</div>
<div class="field abs" style="left:149px;top:2549px;width:435px;height:41px">Email Address*</div>
<div class="field abs" style="left:617px;top:2549px;width:434px;height:41px">Phone Number*</div>
<div class="field msg abs" style="left:149px;top:2617px;width:902px;height:120px">Message*</div>
<div class="btn submit abs">SUBMIT</div>

<div class="foot-brand abs"><span class="name">BROOKVALE</span><span class="sub">INSURANCE SERVICES</span></div>
<div class="contact abs" style="left:111px;top:3110px">
  <div style="display:flex;gap:10px"><svg width="14" height="18" viewBox="0 0 14 18" style="margin-top:4px"><path d="M7 0a7 7 0 0 0-7 7c0 5 7 11 7 11s7-6 7-11a7 7 0 0 0-7-7z" fill="#fff"/></svg><span>7316 Marlowe Ave Unit D, Studio City<br>Ca 91607</span></div>
  <div style="display:flex;gap:10px;margin-top:6px"><svg width="14" height="16" viewBox="0 0 14 16" style="margin-top:5px"><path d="M3 0l3 4-2 2c1 2 3 4 5 5l2-2 3 3-2 3C6 15 0 8 0 3z" fill="#fff"/></svg><span>Phone: (818) 555-0193</span></div>
</div>

<div class="foot-h abs" style="left:489px;top:3015px">Subscribe To Our Newsletter</div>
<div class="foot-p abs" style="left:490px;top:3061px">Subscribe to our newsletter to get the<br>latest update to your indox</div>
<div class="email abs">Email</div>
<div class="send abs"><svg width="62" height="42" viewBox="0 0 62 42"><path d="M22 22l18-9-6 17-4-6z" fill="#fff"/></svg></div>

<div class="foot-h abs" style="left:887px;top:3014px">Follow Us</div>
<div class="social abs" aria-label="Social media links"><span></span><span></span><span></span><span></span></div>
<div class="foot-links abs">Sitemap<br>Privacy Policy<br>Website Accessibility Policy</div>

<div class="rule abs"></div>
<div class="copy abs">© 2024 Brookvale Insurance Services. All Rights Reserved.</div>

</body>
</html>
```